Hop Grower Producer Card

A wisconsin based grower of high quality mid westrn grown Hops with the concept of growing and processing Hops into pellet form for sale to brewers of beer large and small .varieties are grown are Cascade ,Chinook and Centennial

Target Market(s)

Brew masters at micro brews and large breweries

Industry/Entity Type

Processing

Font styles to use
Decorative
Script

Requirements
Must have
• i would like the Hop varieties listed on the back of the card , with the statement Grower of High Quality Wisconsin Hops and the web site address
Nice to have
• german style font for the name Volmer's Bine Lodge

```html
<!DOCTYPE html>
<html lang="en">
<head>
<meta charset="utf-8">
<title>Volmer's Bine Lodge – Hop Varieties Card</title>
<link rel="stylesheet" href="https://fonts.googleapis.com/css2?family=UnifrakturMaguntia&family=Libre+Baskerville&display=swap">
<style>
  :root {
    --card-white: #ffffff;
    --hop-green: #7e9300;
    --edge-dark: #1e2a0c;
    --ink-green: #1f2a10;
    --photo-deep: #3f5a12;
    --photo-mid: #6f8a1e;
    --photo-cone: #a9b6b4;
  }
  html, body {
    margin: 0;
    padding: 0;
    width: 1200px;
    height: 702px;
    overflow: hidden;
    background: var(--card-white);
  }
  .card {
    position: relative;
    width: 1200px;
    height: 702px;
    background: var(--card-white);
    overflow: hidden;
  }
  .corner-band {
    position: absolute;
    inset: 0;
  }
  .variety {
    font-family: "UnifrakturMaguntia", "Old English Text MT", serif;
    font-size: 70px;
    fill: var(--ink-green);
  }
  .web-address {
    font-family: "Libre Baskerville", "Times New Roman", serif;
    font-size: 37px;
    letter-spacing: 2px;
    fill: var(--ink-green);
  }
</style>
</head>
<body>
  <main class="card">
    <svg class="corner-band" width="1200" height="702" viewBox="0 0 1200 702" xmlns="http://www.w3.org/2000/svg">
      <defs>
        <linearGradient id="hop-field-tone" x1="0" y1="0" x2="1" y2="0.6">
          <stop offset="0" stop-color="var(--photo-mid)"/>
          <stop offset="0.35" stop-color="var(--photo-cone)"/>
          <stop offset="0.6" stop-color="var(--photo-deep)"/>
          <stop offset="1" stop-color="var(--photo-cone)"/>
        </linearGradient>
      </defs>
      <polygon class="corner-fill" points="0,0 282,0 0,186" fill="var(--hop-green)"/>
      <polygon class="hop-cones-photo" role="img" aria-label="Photograph of hop cones hanging on the bine, tinted green and grey"
               points="282,0 880,0 0,388 0,186" fill="url(#hop-field-tone)"/>
      <polygon class="band-edge-inner" points="278,0 284,0 0,189 0,185" fill="var(--edge-dark)"/>
      <polygon class="band-edge" points="878,0 892,0 0,398 0,384" fill="var(--edge-dark)"/>

      <g class="varieties" text-anchor="middle">
        <text class="variety" x="887" y="278">Chinook</text>
        <text class="variety" x="887" y="383">Cascade</text>
        <text class="variety" x="887" y="480">Centennial</text>
      </g>
      <text class="web-address" x="880" y="631" text-anchor="middle">www.binelodge34.com</text>
    </svg>
  </main>
</body>
</html>
```